Youtube Graphic Design for Fitness Brand

I own a personal training/fitness brand called Bright Quarry Fitness. I am starting my YouTube channel and need artwork for my banner and an animated intro/outro. For my banner, I would like to see designs that incorporate my brand logo and one of the attached images of me. The point of my channel is to help educate others and help them achieve their fitness goals to live happy balanced lives. The final design should present a high quality fitness brand that offers value to its subscribers. I'd like to keep the project with either a predominately black or white color. Not sure if I have a preference on either color being the dominant color.

Target Market(s)

People looking for help with fitness/healthy lifestyle.

Industry/Entity Type

Fitness

Requirements
Must have
• My logo
Nice to have
• One of the attached photos of me

```html
<!DOCTYPE html>
<html lang="en">
<head>
<meta charset="utf-8">
<title>Bright Quarry Fitness – Channel Banner</title>
<link rel="stylesheet" href="https://fonts.googleapis.com/css2?family=Kanit:ital,wght@1,600&family=Montserrat:wght@700&family=Roboto:wght@300;700&display=swap">
<style>
  :root {
    --ink: #000000;
    --night: #0b0b0c;
    --white: #ffffff;
    --paper: #eeeeee;
    --gold: #ffc400;
    --gold-dim: #8a6a10;
    --steel: #6e6e6e;
    --skin: #c98a6a;
    --shorts: #d8202a;
  }
  * { margin: 0; padding: 0; box-sizing: border-box; }
  html, body { width: 1200px; height: 675px; overflow: hidden; background: var(--ink); }

  .banner { position: relative; width: 1200px; height: 675px; overflow: hidden; }

  .backdrop-photo {
    position: absolute; inset: 0;
    background: radial-gradient(ellipse at 55% 35%, #3a2c28 0%, #1b1a1c 40%, #0e0e10 100%);
  }

  .safe-band { position: absolute; left: 0; top: 239px; width: 1200px; height: 197px; background: var(--ink); overflow: hidden; }
  .band-shapes { position: absolute; inset: 0; }

  .brand-mark {
    position: absolute; left: 197px; top: 251px; width: 100px;
    display: flex; flex-direction: column; align-items: center; gap: 4px;
  }
  .brand-dot { width: 26px; height: 26px; border-radius: 50%; border: 2px solid var(--white); }
  .brand-name {
    font-family: "Montserrat", sans-serif; font-weight: 700; font-size: 6.5px;
    letter-spacing: 1.2px; color: var(--white); white-space: nowrap;
  }

  .tag-workout {
    position: absolute; left: -2px;
    font-family: "Roboto", sans-serif; font-weight: 700; font-size: 42px; line-height: 1;
    letter-spacing: 0.5px;
  }
  .tag-workout--solid {
    top: 345px;
    background: linear-gradient(180deg, #d0d0d0, #6a6a6a);
    -webkit-background-clip: text; background-clip: text; color: transparent;
  }
  .tag-workout--outline {
    top: 378px; color: transparent;
    -webkit-text-stroke: 1px var(--gold-dim);
  }

  .headline {
    position: absolute; font-family: "Kanit", sans-serif; font-style: italic; font-weight: 600;
    font-size: 58px; line-height: 1; letter-spacing: -1px;
  }
  .headline--top { left: 328px; top: 285px; color: var(--white); }
  .headline--bottom { left: 361px; top: 337px; color: var(--gold); }

  .social-list {
    position: absolute; left: 824px; top: 304px; list-style: none;
    font-family: "Roboto", sans-serif; font-weight: 300; font-size: 13.5px; color: var(--ink);
  }
  .social-list li { display: flex; align-items: center; gap: 5px; height: 17.5px; }
  .social-dot { width: 12px; height: 12px; border-radius: 50%; background: var(--ink); }
</style>
</head>
<body>
<div class="banner">
  <div class="backdrop-photo" role="img" aria-label="Blurred dark gym photo of the trainer lifting dumbbells"></div>

  <section class="safe-band">
    <svg class="band-shapes" width="1200" height="197" viewBox="0 0 1200 197">
      <defs>
        <linearGradient id="wave-glow" x1="0" y1="0" x2="1" y2="1">
          <stop offset="0" stop-color="#5a4508"/>
          <stop offset="0.6" stop-color="#1a1405"/>
          <stop offset="1" stop-color="#000"/>
        </linearGradient>
        <linearGradient id="gym-tone" x1="0" y1="0" x2="1" y2="0">
          <stop offset="0" stop-color="#000"/>
          <stop offset="0.3" stop-color="#3a3a3a"/>
          <stop offset="0.7" stop-color="#2a2a2a"/>
          <stop offset="1" stop-color="#000"/>
        </linearGradient>
        <linearGradient id="dot-tone" x1="0" y1="0" x2="1" y2="0">
          <stop offset="0" stop-color="#000"/>
          <stop offset="1" stop-color="#3a2f06"/>
        </linearGradient>
        <linearGradient id="trainer-tone" x1="0" y1="0" x2="0" y2="1">
          <stop offset="0" stop-color="#d29a7a"/>
          <stop offset="0.75" stop-color="#b87255"/>
          <stop offset="0.82" stop-color="#d8202a"/>
          <stop offset="1" stop-color="#b8161f"/>
        </linearGradient>
      </defs>

      <rect class="wave-area" x="0" y="0" width="380" height="110" fill="url(#wave-glow)" opacity="0.55" role="img" aria-label="Flowing gold line pattern"/>
      <rect class="gym-photo" x="328" y="0" width="310" height="197" fill="url(#gym-tone)" role="img" aria-label="Black and white photo of the trainer training in a home gym"/>
      <rect class="gold-dots" x="628" y="0" width="115" height="197" fill="url(#dot-tone)" role="img" aria-label="Gold halftone dot texture"/>

      <polygon class="light-panel" points="741,0 947,0 907,197 741,197" fill="var(--paper)"/>
      <rect class="trainer-photo" x="640" y="6" width="158" height="191" rx="40" fill="url(#trainer-tone)" role="img" aria-label="Photo of the trainer in sunglasses and red shorts"/>

      <polygon class="light-stripe" points="984,0 993,0 961,197 952,197" fill="#d9d9d9"/>

      <g class="diagonal-stripes" stroke="var(--steel)" stroke-width="2.2">
        <line x1="1064" y1="0" x2="1026" y2="197"/>
        <line x1="1072" y1="0" x2="1034" y2="197"/>
        <line x1="1080" y1="0" x2="1042" y2="197"/>
        <line x1="1088" y1="0" x2="1050" y2="197"/>
        <line x1="1096" y1="0" x2="1058" y2="197"/>
        <line x1="1104" y1="0" x2="1066" y2="197"/>
        <line x1="1112" y1="0" x2="1074" y2="197"/>
        <line x1="1120" y1="0" x2="1082" y2="197"/>
        <line x1="1128" y1="0" x2="1090" y2="197"/>
        <line x1="1136" y1="0" x2="1098" y2="197"/>
        <line x1="1144" y1="0" x2="1106" y2="197"/>
        <line x1="1152" y1="0" x2="1114" y2="197"/>
        <line x1="1160" y1="0" x2="1122" y2="197"/>
        <line x1="1168" y1="0" x2="1130" y2="197"/>
        <line x1="1176" y1="0" x2="1138" y2="197"/>
        <line x1="1184" y1="0" x2="1146" y2="197"/>
        <line x1="1192" y1="0" x2="1154" y2="197"/>
        <line x1="1200" y1="0" x2="1162" y2="197"/>
        <line x1="1208" y1="0" x2="1170" y2="197"/>
        <line x1="1216" y1="0" x2="1178" y2="197"/>
        <line x1="1224" y1="0" x2="1186" y2="197"/>
        <line x1="1232" y1="0" x2="1194" y2="197"/>
        <line x1="1240" y1="0" x2="1202" y2="197"/>
      </g>
    </svg>
  </section>

  <div class="brand-mark">
    <span class="brand-dot"></span>
    <span class="brand-name">BRIGHT QUARRY FITNESS</span>
  </div>

  <div class="tag-workout tag-workout--solid">WORKOUT</div>
  <div class="tag-workout tag-workout--outline">WORKOUT</div>

  <h1 class="headline headline--top">HEALTHY</h1>
  <h2 class="headline headline--bottom">LIFESTYLE</h2>

  <ul class="social-list">
    <li><span class="social-dot"></span>/BRIGHTQRY</li>
    <li><span class="social-dot"></span>/BRIGHTQRY</li>
    <li><span class="social-dot"></span>/BRIGHTQRY</li>
  </ul>
</div>
</body>
</html>
```